Elegant Business Cards & Letterhead

We will need the following that need to be designed: Letterhead and Business Cards, there winer will be re-hired for the balance of our stationary needs. Text for the cards and letterheads:

- Corporate Card instead of name
- landline: +971 (4) 362 7041
- mobile: +971 56 2819 605
- 800TUTOR
- email: dubai@velmora-lune.com
- www.velmora-lune.com
- PO Box 387261
Address: Castellan Heights Suite 1708, Dubai UAE

Thank you

Target Market(s)

VIPs, HNWI, High-end Families.

Industry/Entity Type

Luxury Market

Font styles to use
Other font styles liked:
• as explained

Colors

Designer to choose only greyscale colors for use in the design.

Requirements
Must have
• Elegant, Simple, Luxurious, Minimalistic
Nice to have
• Luxury, Golds, Engravings,
Should not have
• Much colors, funky,

```html
<!DOCTYPE html>
<html lang="en">
<head>
<meta charset="utf-8">
<title>Velmora Lune Letterhead</title>
<link href="https://fonts.googleapis.com/css2?family=Marcellus&family=Lato:wght@400;700&family=Montserrat:wght@400&family=Allura&display=swap" rel="stylesheet">
<style>
  :root {
    --backdrop: #8f8f8f;
    --paper: #fbfbfb;
    --ink: #232323;
    --gold-dark: #7a5c17;
    --gold-mid: #b8962f;
    --gold-light: #e2c25a;
  }
  * { margin: 0; padding: 0; box-sizing: border-box; }
  html, body { width: 1200px; height: 1155px; overflow: hidden; }
  body { background: var(--backdrop); position: relative; font-family: "Lato", sans-serif; color: var(--ink); }

  .letterhead {
    position: absolute; left: 205px; top: 19px; width: 790px; height: 1117px;
    background: var(--paper); box-shadow: 0 6px 24px rgba(0,0,0,.35); overflow: hidden;
  }

  .edge { position: absolute; left: 0; width: 790px; }
  .edge--top { top: 0; }
  .edge--bottom { bottom: 0; }
  .edge__band {
    height: 26px;
    background: linear-gradient(90deg, var(--gold-dark), var(--gold-light) 50%, var(--gold-dark));
  }
  .edge__rule {
    height: 1px; margin: 6px 48px 0;
    background: var(--gold-mid);
  }
  .edge--bottom .edge__rule { margin: 0 48px 6px; }

  .brand-name {
    position: absolute; left: 70px; top: 86px;
    font-family: "Marcellus", serif; font-weight: 400; font-size: 40px; letter-spacing: 2px;
    color: var(--gold-mid);
  }

  .contact {
    position: absolute; left: 505px; top: 62px; padding-left: 12px;
    border-left: 1px solid var(--gold-mid);
    font-family: "Montserrat", sans-serif; font-style: normal; font-size: 11.5px; line-height: 1.45;
  }
  .contact__row { display: flex; align-items: center; gap: 7px; }
  .contact__row svg { width: 11px; height: 11px; flex: none; }

  .letter { position: absolute; left: 88px; top: 330px; width: 600px; font-size: 14px; }
  .letter__date { margin-bottom: 18px; }
  .letter__recipient { margin-left: 14px; line-height: 1.3; margin-bottom: 14px; }
  .letter__company { margin-left: 28px; line-height: 1.3; margin-bottom: 18px; }
  .letter__salutation { font-weight: 700; font-size: 17px; margin: 0 0 14px 40px; }
  .letter__body p { margin: 0 0 18px 40px; line-height: 1.35; text-align: justify; width: 560px; }
  .letter__closing { margin: 46px 0 0 70px; }
  .letter__signature { font-family: "Allura", cursive; font-size: 48px; line-height: 1.1; margin: 4px 0 0 90px; }
</style>
</head>
<body>
  <main class="letterhead">
    <div class="edge edge--top" aria-hidden="true">
      <div class="edge__band"></div>
      <div class="edge__rule"></div>
    </div>

    <h1 class="brand-name">VELMORA LUNE</h1>

    <address class="contact">
      <div>Castellan Heights Suite 1708,<br>PO Box 387261, Dubai UAE</div>
      <div class="contact__row">
        <svg viewBox="0 0 12 12" aria-hidden="true"><path d="M2 1l2 0 1 3-1.5 1a6 6 0 0 0 3 3L7.5 6.5l3 1 0 2A1.5 1.5 0 0 1 9 11 8 8 0 0 1 1 3 1.5 1.5 0 0 1 2 1z" fill="#b8962f"/></svg>
        +971 (4) 362 7041
      </div>
      <div class="contact__row">
        <svg viewBox="0 0 12 12" aria-hidden="true"><rect x="1" y="2.5" width="10" height="7" fill="#b8962f"/><path d="M1 2.5l5 4 5-4" stroke="#fbfbfb" fill="none"/></svg>
        dubai@velmora-lune.com
      </div>
      <div class="contact__row">
        <svg viewBox="0 0 12 12" aria-hidden="true"><circle cx="6" cy="6" r="5" fill="#b8962f"/><path d="M1 6h10M6 1c-3 3-3 7 0 10M6 1c3 3 3 7 0 10" stroke="#fbfbfb" stroke-width=".7" fill="none"/></svg>
        www.velmora-lune.com
      </div>
    </address>

    <article class="letter">
      <p class="letter__date">Feb-03-2022</p>
      <p class="letter__recipient">Mr, Adrian Vell<br>President</p>
      <p class="letter__company">Corvane Holdings<br>48 Harbour Lane, Suite# 6<br>Dubai, UAE, 387261</p>
      <p class="letter__salutation">Dear Mr, Adrian</p>
      <div class="letter__body">
        <p>Lorem ipsum dolor sit amet, consectetur adipisicing elit, sed do eiusmod tempor incididunt ut labore et dolore magna aliqua. Ut enim ad minim veniam, quis nostrud exercitation ullamco laboris nisi ut aliquip ex ea commodo consequat. Duis aute irure dolor in reprehenderit in voluptate velit esse cillum dolore eu fugiat nulla pariatur.</p>
        <p>Lorem ipsum dolor sit amet, consectetur adipisicing elit, sed do eiusmod tempor incididunt ut labore et dolore magna aliqua. Ut enim ad minim veniam, quis nostrud exercitation ullamco laboris nisi ut aliquip ex ea commodo consequat. Duis aute irure dolor in reprehenderit in voluptate velit esse cillum dolore eu fugiat nulla pariatur.</p>
        <p>Lorem ipsum dolor sit amet, consectetur adipisicing elit, sed do eiusmod tempor incididunt ut labore et dolore magna aliqua. Ut enim ad minim veniam, quis nostrud exercitation ullamco laboris nisi ut aliquip ex ea commodo consequat.</p>
        <p>Excepteur sint occaecat cupidatat non proident, sunt in culpa qui officia deserunt mollit anim id est laborum. re et dolore magnam aliquam quaerat voluptatem.</p>
      </div>
      <p class="letter__closing">Regards</p>
      <p class="letter__signature">Julian Ardent</p>
    </article>

    <div class="edge edge--bottom" aria-hidden="true">
      <div class="edge__rule"></div>
      <div class="edge__band"></div>
    </div>
  </main>
</body>
</html>
```